Business cards and logo for kitchen and bath remodeling company

We want an elegant card but that calls attention something unique and when people see it they remember us. A log that we can use for our own. We are a kitchen and bathroom remodeling company. We are 3 partners staring the company we are located in seattle washington usa. We try to give the best experience and luxury look in our projects and we are looking to show that in our cards. I added a sample of a card I really like. I like the black and gold look but gray blue or green in a metallic look would look nice. I'm open to any color.

Target Market(s)

Home owners.

Industry/Entity Type

Construction

Contact Information for Business Card

Larchmont and Vey builders

Colors

Designer to choose colors to be used in the design.

Requirements
Must have
• Make a Logo
• Logo to be unique
• Name of company larchmont and vey builders
Nice to have
• Have a good color scheme
• Front design to connect with back of card

```html
<!DOCTYPE html>
<html lang="en">
<head>
<meta charset="utf-8">
<title>Larchmont and Vey Builders — Business Cards</title>
<link rel="stylesheet" href="https://fonts.googleapis.com/css2?family=Montserrat:wght@600&family=Arimo:wght@400;700&display=swap">
<style>
  :root {
    --backdrop: #3b3532;
    --card: #0d0d0d;
    --card-edge: #1c1c1c;
    --gold: #c9a77a;
    --silver: #d6d6d6;
    --text-light: #cfcfcf;
    --divider: #2e2e2e;
  }
  * { box-sizing: border-box; margin: 0; padding: 0; }
  html, body { width: 1200px; height: 844px; overflow: hidden; }
  body {
    background: var(--backdrop);
    position: relative;
    font-family: "Arimo", Arial, sans-serif;
  }
  .card {
    position: absolute;
    top: 273px;
    width: 520px;
    height: 298px;
    background: var(--card);
    border: 1px solid var(--card-edge);
    border-radius: 3px;
  }
  .card--back { left: 60px; display: flex; }
  .card--front { left: 620px; display: flex; align-items: center; justify-content: center; }

  .brand {
    display: flex;
    flex-direction: column;
    align-items: center;
    gap: 14px;
  }
  .brand__mark { width: 34px; height: 34px; border: 3px solid currentColor; }
  .brand__name {
    font-family: "Montserrat", Arial, sans-serif;
    font-weight: 600;
    font-size: 17px;
    letter-spacing: 0.5px;
    text-transform: uppercase;
    text-align: center;
    line-height: 1.35;
  }
  .brand__rule { width: 150px; height: 1px; background: currentColor; opacity: 0.6; }
  .brand--gold { color: var(--gold); }
  .brand--silver { color: var(--silver); }

  .back__brand-panel {
    width: 290px;
    display: flex;
    align-items: center;
    justify-content: center;
    border-right: 1px solid var(--divider);
  }
  .contact {
    flex: 1;
    padding: 58px 0 0 24px;
    color: var(--text-light);
    font-size: 13px;
    line-height: 1.35;
  }
  .contact__name {
    color: var(--gold);
    font-weight: 700;
    font-size: 15px;
    letter-spacing: 0.3px;
    text-transform: uppercase;
  }
  .contact__title { margin-bottom: 6px; }
  .contact__list { list-style: none; }
  .contact__item { display: flex; align-items: center; gap: 8px; }
  .contact__icon { width: 10px; height: 10px; fill: var(--text-light); flex: none; }
  .contact__address { margin-top: 12px; }
</style>
</head>
<body>
  <section class="card card--back">
    <div class="back__brand-panel">
      <div class="brand brand--gold">
        <span class="brand__mark"></span>
        <p class="brand__name">Larchmont and Vey<br>Builders</p>
        <span class="brand__rule"></span>
      </div>
    </div>
    <div class="contact">
      <p class="contact__name">Adrian Kessel</p>
      <p class="contact__title">Managing Director</p>
      <ul class="contact__list">
        <li class="contact__item">
          <svg class="contact__icon" viewBox="0 0 10 10" aria-hidden="true"><path d="M1 3 Q5 0 9 3 L8 4.5 L6.5 3.8 L6.5 3 Q5 2.6 3.5 3 L3.5 3.8 L2 4.5 Z M2 5 H8 L8.5 9 H1.5 Z"/></svg>
          206-318 5529
        </li>
        <li class="contact__item">
          <svg class="contact__icon" viewBox="0 0 10 10" aria-hidden="true"><path d="M0.5 2 H9.5 V8 H0.5 Z M1 2.5 L5 5.5 L9 2.5" stroke="#0d0d0d" stroke-width="0.8"/></svg>
          hello@larchvey.com
        </li>
        <li class="contact__item">
          <svg class="contact__icon" viewBox="0 0 10 10" aria-hidden="true"><circle cx="5" cy="5" r="4.5"/></svg>
          www.larchvey.com
        </li>
      </ul>
      <p class="contact__address">87, Harbor Lane Northwest<br>98107, Washington</p>
    </div>
  </section>

  <section class="card card--front">
    <div class="brand brand--silver">
      <span class="brand__mark"></span>
      <p class="brand__name">Larchmont and Vey<br>Builders</p>
      <span class="brand__rule"></span>
    </div>
  </section>
</body>
</html>
```